Business Management System Providor Needs Upscale Business Card Design

We provide an online Claims Management System to the Insurance Industry called Meridel Casework Suite. Although our core offering is claims management, our system provides full business management features including reporting, invoicing, business trend analysis, etc..
We have a worldwide client base and our system has become known for its reliability, rich feature set, and intuitive design. This being the case we would like our cards to maintain a high level of professionalism. We have a tendency to lean toward a corporate look and feel and we would like to maintain that image.
Current Site: www.merideldesk-example.com
Target Market(s)
Big Business, Insurance Professionals, Corporate Organizations
Industry/Entity Type
Business Management
Look and feel
Each slider illustrates characteristics of the customer's brand and the style your logo design should communicate.

```html
<!DOCTYPE html>
<html lang="en">
<head>
<meta charset="utf-8">
<title>Meridel Casework Suite – Business Card</title>
<link rel="stylesheet" href="https://fonts.googleapis.com/css2?family=Roboto:wght@400;500;700&display=swap">
<style>
  :root {
    --navy: #173a64;
    --navy-deep: #12315a;
    --grey: #7b7f85;
    --grey-light: #a7abb0;
    --paper: #ffffff;
    --backdrop: #ececec;
    --rule: #8d9196;
  }
  * { margin: 0; padding: 0; box-sizing: border-box; }
  html, body { width: 1200px; height: 720px; overflow: hidden; }
  body {
    background: var(--backdrop);
    font-family: "Roboto", Arial, sans-serif;
    display: flex; align-items: center; justify-content: center; gap: 48px;
  }
  .card {
    width: 504px; height: 288px; position: relative; overflow: hidden;
    box-shadow: 0 6px 18px rgba(0,0,0,.12);
  }
  /* Front */
  .card--front {
    background: radial-gradient(circle at 45% 45%, #1d4574 0%, var(--navy-deep) 70%);
    display: flex; flex-direction: column; align-items: center; justify-content: center;
    color: var(--paper);
  }
  .brand { display: flex; align-items: center; gap: 14px; }
  .brand__square { width: 54px; height: 54px; border-radius: 8px; background: var(--paper); flex: none; }
  .brand__name { font-weight: 700; font-size: 26px; line-height: 1.05; }
  .tagline { margin-top: 12px; font-size: 17px; letter-spacing: .2px; }
  /* Back */
  .card--back { background: var(--paper); }
  .back__brand { position: absolute; left: 26px; top: 26px; color: var(--navy); }
  .back__brand .brand__square { width: 46px; height: 46px; background: var(--navy); }
  .back__brand .brand__name { font-size: 19px; }
  .back__tagline { position: absolute; left: 88px; top: 82px; font-size: 12.5px; color: var(--grey); }
  .person { position: absolute; right: 28px; top: 28px; text-align: right; }
  .person__name { font-size: 20px; font-weight: 500; color: var(--navy); }
  .person__title { font-size: 11px; color: var(--grey); padding-bottom: 4px; border-bottom: 1px solid var(--rule); margin-top: 2px; width: 210px; }
  .contacts { position: absolute; right: 28px; top: 108px; list-style: none; text-align: right; font-size: 11px; color: var(--grey); line-height: 16px; }
  .contacts li { display: flex; justify-content: flex-end; align-items: center; gap: 5px; }
  .contacts svg { width: 9px; height: 9px; fill: var(--grey); }
  .contacts .gap { margin-top: 10px; }
  .address {
    position: absolute; left: 26px; top: 180px; width: 220px;
    border-top: 1px solid var(--rule); padding-top: 8px;
    font-size: 11px; color: var(--grey); line-height: 14px; font-style: normal;
  }
  .band { position: absolute; left: 0; right: 0; bottom: 0; height: 26px; background: var(--navy); border-top: 5px solid var(--grey-light); }
</style>
</head>
<body>
  <section class="card card--front" aria-label="Card front">
    <div class="brand">
      <span class="brand__square"></span>
      <span class="brand__name">Meridel<br>Casework Suite</span>
    </div>
    <p class="tagline">claim management systems</p>
  </section>

  <section class="card card--back" aria-label="Card back">
    <div class="brand back__brand">
      <span class="brand__square"></span>
      <span class="brand__name">Meridel<br>Casework Suite</span>
    </div>
    <p class="back__tagline">claim management systems</p>

    <div class="person">
      <p class="person__name">Dana Whitlock</p>
      <p class="person__title">Director of Software Development</p>
    </div>

    <ul class="contacts">
      <li>555-014-2270 x114
        <svg viewBox="0 0 10 10"><path d="M2 1h2l1 2-1.2 1a6 6 0 0 0 2.2 2.2L7 5l2 1v2l-1 1C4.5 9 1 5.5 1 2z"/></svg></li>
      <li>555-019-4410
        <svg viewBox="0 0 10 10"><rect x="1" y="4" width="8" height="5" rx="1"/><rect x="3" y="1" width="4" height="3"/></svg></li>
      <li class="gap">dwhitlock@merideldesk-example.com
        <svg viewBox="0 0 10 10"><path d="M1 2h8v6H1z M1 2l4 3 4-3" stroke="#fff" stroke-width=".8"/></svg></li>
      <li>www.merideldesk-example.com
        <svg viewBox="0 0 10 10"><circle cx="5" cy="5" r="4"/><path d="M1 5h8M5 1v8" stroke="#fff" stroke-width=".7"/></svg></li>
    </ul>

    <address class="address">
      1180 Alder Crest Road<br>
      Suite 400<br>
      Northbrook, ON,<br>
      Canada, K0A 3Z9
    </address>

    <div class="band"></div>
  </section>
</body>
</html>
```